Vacation/Holiday Home Wordpress Website

I currently have a website for our vacation/holiday rental home. It is 6 years old and needs a complete redesign to acommodate many new features available today. The existing website can be seen at www.coralbaystayrentals.co.uk . The purpose of the website is mainly to provide useful infomation about our home, the destination of Barbados. The customer is also able to check availability and book. Please note that there is a booking element to the website which is hosted externally. This can be seen at

http://stays.reservo-planner.net/PickArrival_Slim.asp?ref=kWT%3DHJRN%26QWT%3DMPLL

I now wish to add key functionality such as:

- Video of property and area
- Customer video testimonials
- Other useful information

The navigation, menus and buttons need to be re designed to give a modern, innovative and professional look and feel.

My customers are mainly females between the ages of 35 and 55. The website needs to reassure customers who are parting with a lot of mony by booking online. It needs to give a sense of trust as this may be a once in a lifetime trip which they have saved up for for a long time. Many visitors to the website will be referred by other websites such as www.nestroam.co.uk and www.villatrove.co.uk.
Updates

Dear designers, 

Thank you for taking the time to write some further comments to you all. 

1. The homepage should have an availability search function as a key feature

2. The look and feel does NOT need to have the 3 feature columns like my current website has

3.  There should not be too much text on the homepage. Brief text can be included with 'more'  buttons to reveal more information 

4.  For designs that are under consideration, we will need to see a design for the other pages as they will be different to the homepage. Information from other pages on the existing website can be used. 

Reason: Dear all, I will be providing extensive feedback later today following a review that we have conducted with a group of our guests. To enable you to read and use this information, we have extended the deadline by 5 days. Thank you for the design submisions so far. We hope that the additional feedback will enable you to amend your designs appropriately. Regards Martin Fenwick

Dear all,

Thank you for your designs.  I apologise that I am unable to give detailed feedback on each and every design submitted.  I will contact you individually and indicate whether we would like you to submit any further designs.  These should take into account the feedback below.

Feedback from design review group

1.  Logo should not be displayed in a white box.  It should blend in with the background or be overlayed onto the picture.

2.  There must be an availability calendar on the home page.

3.  Any background image should be subtle, maybe blurred and not distract from the main area.

4.  Text should be limited to a few key words with a 'read more' button to reveal more information.

5.  A gallery/slide show should be featured in the top part of the screen

6.  Icons can be used as navigation buttons

7.  Video testimonials is a key feature and should appear on the home page

8.   The use of bold and vibrant colours is preferred

9.   The 3 column format of the old website should not be copied

Regards

Martin

Target Market(s)

Female's, Families, 35 to 55 year olds, travellers to Barbados

Industry/Entity Type

Online

Requirements
Must have
• Pictures
Video
Testimonials
Clear and stylish navigation
Easy to use navigation
Should not have
• Dated look or feel

```html
<!DOCTYPE html>
<html lang="en">
<head>
<meta charset="utf-8">
<title>Coral Bay Stay Rentals</title>
<link rel="stylesheet" href="https://fonts.googleapis.com/css2?family=Arimo:wght@400;700&family=PT+Sans:ital,wght@0,400;0,700;1,700&display=swap">
<style>
:root{
  --red:#ea3a2b;
  --red-dark:#c92a1d;
  --blue:#1a73b8;
  --ink:#2b2b2b;
  --line:#bdbdbd;
  --page:#ece9e9;
  --white:#fff;
  --footer:#353535;
  --footer-text:#f2f2f2;
  --card:#f4f4f4;
}
*{box-sizing:border-box;margin:0;padding:0}
html,body{width:1200px;height:1192px;overflow:hidden}
body{background:var(--page);font-family:Arimo,Arial,sans-serif;color:var(--ink);position:relative}
.abs{position:absolute}
.sheet{position:absolute;left:101px;top:0;width:997px;height:1192px;background:var(--white)}
.header{position:absolute;left:101px;top:0;width:997px;height:130px;background:linear-gradient(#f4f4f4,#fff)}
.brand{left:120px;top:62px;font-family:"PT Sans",sans-serif;font-size:26px;font-weight:700;letter-spacing:2px;color:var(--red);display:flex;align-items:center;gap:10px}
.brand-dot{width:22px;height:22px;border-radius:50%;background:var(--red)}
.phone{left:884px;top:30px;display:flex;align-items:center;gap:10px;font-family:"PT Sans",sans-serif;font-size:18px;color:#444;letter-spacing:.5px}
.stay{left:820px;top:88px;font-family:"PT Sans",sans-serif;font-style:italic;font-weight:700;font-size:14px;color:var(--blue)}
.social{left:938px;top:78px;display:flex;gap:8px}
.social span{width:32px;height:32px;border-radius:50%}
.nav{left:108px;top:137px;width:983px;height:42px;background:var(--red);border-radius:4px;display:flex;font-family:"PT Sans",sans-serif;font-size:16px;color:var(--white)}
.nav a{color:inherit;text-decoration:none;display:flex;align-items:center;justify-content:center;border-right:1px solid var(--red-dark);height:100%}
.nav a:last-child{border-right:0}
.hero{left:108px;top:187px;width:983px;height:318px;border:1px solid #ddd;padding:1px}
.hero-img{width:100%;height:100%;background:linear-gradient(180deg,#2f8fe0 0%,#7cc3f0 48%,#2fd0d9 58%,#8de6e6 72%,#f1f4f2 100%)}
.search{left:137px;top:254px;width:536px;height:105px;background:rgba(255,255,255,.93);border-radius:3px;padding:15px 14px}
.search h1{font-weight:400;font-size:19px;color:var(--blue);white-space:nowrap}
.search-row{display:flex;align-items:center;margin-top:19px;font-size:14px;gap:10px}
.date{width:114px;height:22px;background:#fff;border:1px solid #e2e2e2;font-size:12px;display:flex;align-items:center;justify-content:space-between;padding:0 4px 0 7px}
.cal{width:19px;height:14px;border:2px solid #7ccbd0;border-radius:3px;background:#dff4f5}
.btn{background:var(--red);color:#fff;font-size:12px;padding:5px 5px;border-radius:4px;margin-left:4px}
.section-title{font-size:18px;font-weight:400;letter-spacing:.2px;white-space:nowrap}
.blue{color:var(--blue)}.red{color:var(--red)}
.rule{height:0;border-top:1px dashed var(--line)}
.intro{left:127px;top:594px;width:602px;font-size:12px;line-height:18px;text-align:justify;color:#333}
.intro p{height:72px;overflow:hidden}
.intro p+p{margin-top:23px}
.video{border:5px solid #222;background:#222}
.video-img{width:100%;background:linear-gradient(135deg,#f3f0ea 0%,#d9d2c6 35%,#7fa75a 50%,#c2703d 75%,#3a2a20 100%)}
.controls{height:12px;background:#1b1b1b;display:flex;align-items:center;padding:0 4px;gap:5px}
.controls .bar{flex:1;height:3px;background:#666}
.controls .bar i{display:block;width:20%;height:100%;background:var(--red)}
.controls .t{font-size:6px;color:#ccc}
.play{position:absolute;left:50%;top:50%;transform:translate(-50%,-50%)}
.card{border:1px solid #ddd;border-radius:4px;background:linear-gradient(#fff,var(--card))}
.card h2{position:absolute;font-size:18px;font-weight:400;white-space:nowrap;top:16px}
.card .rule{position:absolute;top:43px}
.list{list-style:none;font-size:12px;color:#333;position:absolute}
.list li{position:relative;padding-left:12px;height:21px;white-space:nowrap}
.list li::before{content:"";position:absolute;left:0;top:4px;border-left:4px solid #333;border-top:3.5px solid transparent;border-bottom:3.5px solid transparent}
.list.tight li{height:20px}
.footer{left:101px;top:1090px;width:997px;height:102px;background:var(--footer);color:var(--footer-text);font-size:12px}
.footer span{position:absolute;top:30px;white-space:nowrap}
.footer-brand{left:794px;top:52px;font-family:"PT Sans",sans-serif;font-size:18px;letter-spacing:3px;color:#bbb;display:flex;align-items:center;gap:8px}
</style>
</head>
<body>
<div class="sheet"></div>
<header class="header"></header>

<div class="abs brand"><span class="brand-dot"></span>CORAL BAY STAY RENTALS</div>

<div class="abs phone">
  <svg width="34" height="22" viewBox="0 0 34 22" aria-hidden="true"><path d="M2 8 Q17 -3 32 8 L29 12 L23 9 L23 6 Q17 4 11 6 L11 9 L5 12 Z" fill="#ea3a2b"/><rect x="9" y="11" width="16" height="10" rx="2" fill="#ea3a2b"/><circle cx="17" cy="15.5" r="3" fill="#fff"/></svg>
  <span>: 01-462-3958</span>
</div>
<div class="abs stay">Stay Connected</div>
<div class="abs social">
  <span style="background:#3b5a9a"></span>
  <span style="background:#2aa4e0"></span>
  <span style="background:#e5432f"></span>
</div>

<nav class="abs nav">
  <a href="#" style="width:107px">Home</a>
  <a href="#" style="width:211px">Solmara Holiday Home</a>
  <a href="#" style="width:122px">Local Area</a>
  <a href="#" style="width:132px">Book Now</a>
  <a href="#" style="width:121px">Price</a>
  <a href="#" style="width:150px">Testimonial</a>
  <a href="#" style="width:140px">Contact us</a>
</nav>

<div class="abs hero">
  <div class="hero-img" role="img" aria-label="Photo of a white sand beach with turquoise sea, palm trees and a beachfront villa"></div>
</div>
<div class="abs search">
  <h1>Solmara - Stunning home close to Miami / Enterprise beach!</h1>
  <div class="search-row">
    <span>Start Date</span><span class="date">DD/MM/YYYY<i class="cal"></i></span>
    <span>Start Date</span><span class="date">DD/MM/YYYY<i class="cal"></i></span>
    <span class="btn">Check Availability</span>
  </div>
</div>

<h2 class="abs section-title" style="left:130px;top:537px"><span class="blue">WELCOME TO </span><span class="red">CORAL BAY STAY RENTALS</span></h2>
<div class="abs rule" style="left:129px;top:575px;width:597px"></div>
<div class="abs intro">
  <p><b>Lorem Ipsum is simply dummy text of the printing and typesetting industry.</b> Lorem Ipsum has been the indus&shy;try's standard dummy text ever since the 1500s, when an unknown printer took a galley of type and scrambled it to make a type specimen book. It has survived not only five centuries, but also the leap into electronic typesetting, remaining essentially unchanged. It was popularised in the 1960s with the release of sheets containing</p>
  <p><b>Lorem Ipsum is simply dummy text of the printing and typesetting industry.</b> Lorem Ipsum has been the indus&shy;try's standard dummy text ever since the 1500s, when an unknown printer took a galley of type and scrambled it to make a type specimen book. It has survived not only five centuries, but also the leap into electronic typesetting, remaining essentially unchanged. It was popularised in the 1960s with the release of sheets containing</p>
</div>

<h2 class="abs section-title red" style="left:842px;top:537px">WATCH VIDEO</h2>
<div class="abs video" style="left:776px;top:572px;width:300px;height:196px">
  <div class="video-img" style="height:174px;position:relative" role="img" aria-label="Video still of the villa living room opening onto a garden patio">
    <svg class="play" width="50" height="50" viewBox="0 0 50 50" aria-hidden="true"><circle cx="25" cy="25" r="23" fill="rgba(40,40,40,.75)" stroke="#eee" stroke-width="3"/><path d="M19 14 L36 25 L19 36 Z" fill="#fff"/></svg>
  </div>
  <div class="controls"><span class="t">▶</span><span class="bar"><i></i></span><span class="t">00:01 / 10:01</span></div>
</div>

<section class="abs card" style="left:121px;top:813px;width:308px;height:240px">
  <h2 style="left:70px"><span class="blue">Top 10 </span><span class="red">Attractions</span></h2>
  <div class="rule" style="left:14px;width:274px"></div>
  <ul class="list tight" style="left:9px;top:64px">
    <li>Miami/Enterprise Beach</li>
    <li>Coastline Jeep Safari</li>
    <li>Island Drum Nights</li>
    <li>The Bay Skipper</li>
    <li>Reefdeep Submarines</li>
    <li>Crystal Grotto Cave</li>
    <li>Sandhill Golf Club</li>
    <li>Black Flag Cruise</li>
  </ul>
  <ul class="list tight" style="left:170px;top:67px">
    <li>Old Cask Rum Tour</li>
    <li>Tidewave Cruises</li>
  </ul>
</section>

<section class="abs card" style="left:446px;top:813px;width:308px;height:240px">
  <h2 style="left:87px"><span class="blue">House </span><span class="red">Features</span></h2>
  <div class="rule" style="left:18px;width:274px"></div>
  <ul class="list tight" style="left:34px;top:58px">
    <li>Two luxurious air conditioned bedrooms</li>
    <li>Sleeps 4 Persons, 3 bathrooms</li>
    <li>Luxuriously furnished to highest standard</li>
    <li>Wireless broadband and Personal Computer</li>
    <li>Motion-play games console</li>
    <li>Private patio overlooking tropical landscape</li>
    <li>Secure community of only 6 houses</li>
    <li>2 beaches within 8 minutes walk</li>
  </ul>
</section>

<section class="abs card" style="left:769px;top:813px;width:309px;height:240px">
  <h2 style="left:80px"><span class="blue">Clintes </span><span class="red">Testimonials</span></h2>
  <div class="rule" style="left:22px;width:274px"></div>
  <div class="abs video" style="left:42px;top:63px;width:233px;height:152px;border-width:4px">
    <div class="video-img" style="height:132px;position:relative;background:linear-gradient(135deg,#c9ccc9,#8b8f8a 40%,#b13a30 60%,#2a2a2a)" role="img" aria-label="Video testimonial from guests reviewing their booking">
      <svg class="play" width="40" height="40" viewBox="0 0 50 50" aria-hidden="true"><circle cx="25" cy="25" r="23" fill="rgba(60,60,60,.7)"/><path d="M19 14 L36 25 L19 36 Z" fill="#fff"/></svg>
    </div>
    <div class="controls"><span class="t">▶</span><span class="bar"><i></i></span><span class="t">00:01 / 10:01</span></div>
  </div>
</section>

<footer class="abs footer">
  <span style="left:21px">Home</span><span style="left:70px">|</span>
  <span style="left:89px">Solmara Holiday Home</span><span style="left:226px">|</span>
  <span style="left:249px">Local Area</span><span style="left:326px">|</span>
  <span style="left:353px">Book Now</span><span style="left:431px">|</span>
  <span style="left:451px">Price</span><span style="left:505px">|</span>
  <span style="left:532px">Testimonial</span><span style="left:616px">|</span>
  <span style="left:636px">Contact us</span>
  <span style="left:20px;top:66px">Copyright CORAL BAY 2013 -2014</span>
  <div class="abs footer-brand"><i style="width:14px;height:14px;border-radius:50%;background:#bbb"></i>CORAL BAY</div>
</footer>
</body>
</html>
```